Seeking funky, innovative business cards

I am looking to refresh our current business cards to something more engaging, visual and impactful. We are a management consultancy firm, see website (www.larkspur-advisory.com.au). I've included our colour scheme, sample of the slides we use and our old business cards. We would like our cards to have icons. The card should display:- Name- Title- Mobile number- Address- Email address- Website - Company logo- Our purpose statement "We create the best places on earth to work"

Contact Information for Business Card

Tavish Brellan
Consultant
0491 672 348
Level 5, 218 Warrick Lane, Melbourne 3000
tavish@larkspur-advisory.com.au
www.larkspur-advisory.com.au

Purpose statement "we create the best places on earth to work"
LOGO available in google images

Font styles to use
Other font styles liked:
• Open Sans Light, Bebas Neue (open to other cool foints)

Colors
ffc214
5c5c5c
f5f5f5
fefefe

Requirements
Must have
• - Name
• - Title
• - Mobile number
• - Address
• - Email address
• - Website
• - Company logo
• - Our purpose statement "We create the best places on earth to work"
Nice to have
• - Icons
• - Colour (see our colour scheme"

```html
<!DOCTYPE html>
<html lang="en">
<head>
<meta charset="utf-8">
<title>Larkspur Advisory – Business Card</title>
<link rel="stylesheet" href="https://fonts.googleapis.com/css2?family=Open+Sans:wght@300;400;600;700&display=swap">
<style>
  :root {
    --brand-yellow: #ffc214;
    --brand-grey: #5c5c5c;
    --backdrop: #f0f0f0;
    --card-white: #fefefe;
    --tagline-orange: #f7a21b;
    --soft-white: #f5f5f5;
  }
  * { margin: 0; padding: 0; box-sizing: border-box; }
  html, body {
    width: 1200px; height: 848px; overflow: hidden;
    background: var(--backdrop);
    font-family: "Open Sans", Arial, sans-serif;
  }
  .canvas { position: relative; width: 1200px; height: 848px; }

  .card {
    position: absolute; left: 338px; width: 524px; height: 320px;
    box-shadow: 6px 8px 14px rgba(0,0,0,0.22);
    overflow: hidden;
  }

  /* Front */
  .card-front { top: 88px; display: flex; border: 1px solid #d6d6d6; }
  .front-brand {
    width: 235px; background: var(--card-white);
    position: relative;
  }
  .brand-mark {
    position: absolute; left: 28px; top: 98px;
    display: flex; align-items: center; gap: 8px;
  }
  .brand-dot {
    width: 12px; height: 12px; border-radius: 50%;
    background: var(--brand-yellow); flex: none;
  }
  .brand-name {
    font-size: 28px; font-weight: 400; line-height: 1.05;
    color: var(--brand-grey); letter-spacing: -0.5px;
  }
  .brand-tagline {
    position: absolute; left: 56px; top: 208px;
    font-size: 12.5px; font-weight: 600; color: var(--tagline-orange);
    letter-spacing: -0.1px;
  }
  .front-details {
    flex: 1; background: var(--brand-grey); color: var(--soft-white);
    padding: 94px 0 0 28px;
  }
  .person-name { font-size: 23px; font-weight: 400; color: var(--brand-yellow); line-height: 1.2; }
  .person-title { font-size: 14px; font-weight: 400; margin-top: 4px; }
  .contact-list { list-style: none; margin-top: 26px; }
  .contact-item {
    display: flex; align-items: flex-start; gap: 10px;
    font-size: 13.5px; line-height: 17px; margin-bottom: 9px;
  }
  .contact-icon { width: 14px; height: 14px; flex: none; margin-top: 1px; fill: var(--brand-yellow); }

  /* Back */
  .card-back { top: 445px; }
  .back-brand {
    height: 258px; background: var(--brand-yellow);
    display: flex; align-items: center; justify-content: center; gap: 14px;
    padding-top: 20px;
  }
  .back-brand .brand-dot { width: 18px; height: 18px; background: var(--card-white); }
  .back-brand .brand-name { font-size: 58px; font-weight: 300; color: var(--card-white); letter-spacing: -1px; }
  .purpose-band {
    height: 62px; background: var(--brand-grey); color: var(--card-white);
    display: flex; align-items: center; justify-content: center;
    font-size: 14px; font-weight: 700; text-transform: uppercase; letter-spacing: 0.2px;
  }
</style>
</head>
<body>
<main class="canvas">

  <section class="card card-front">
    <div class="front-brand">
      <div class="brand-mark">
        <span class="brand-dot"></span>
        <span class="brand-name">Larkspur<br>Advisory</span>
      </div>
      <p class="brand-tagline">Strategy. People. Impact.</p>
    </div>
    <div class="front-details">
      <h1 class="person-name">Tavish Brellan</h1>
      <p class="person-title">Consultant</p>
      <ul class="contact-list">
        <li class="contact-item">
          <svg class="contact-icon" viewBox="0 0 24 24"><path d="M12 2a7 7 0 0 0-7 7c0 5.2 7 13 7 13s7-7.8 7-13a7 7 0 0 0-7-7zm0 9.5A2.5 2.5 0 1 1 12 6.5a2.5 2.5 0 0 1 0 5z"/></svg>
          <span>Level 5, 218 Warrick Lane,<br>Melbourne 3000</span>
        </li>
        <li class="contact-item">
          <svg class="contact-icon" viewBox="0 0 24 24"><path d="M6.6 10.8a15.1 15.1 0 0 0 6.6 6.6l2.2-2.2a1 1 0 0 1 1-.25 11.4 11.4 0 0 0 3.6.57 1 1 0 0 1 1 1V20a1 1 0 0 1-1 1A17 17 0 0 1 3 4a1 1 0 0 1 1-1h3.5a1 1 0 0 1 1 1c0 1.25.2 2.45.57 3.57a1 1 0 0 1-.25 1z"/></svg>
          <span>0491 672 348</span>
        </li>
        <li class="contact-item">
          <svg class="contact-icon" viewBox="0 0 24 24"><path d="M2 5h20v14H2z"/><path d="M2 5l10 7 10-7" fill="none" stroke="#5c5c5c" stroke-width="1.6"/></svg>
          <span>tavish@larkspur-advisory.com.au</span>
        </li>
        <li class="contact-item">
          <svg class="contact-icon" viewBox="0 0 24 24"><circle cx="12" cy="12" r="10"/><path d="M2 12h20M12 2c3 3 3 17 0 20M12 2c-3 3-3 17 0 20M4 7h16M4 17h16" fill="none" stroke="#5c5c5c" stroke-width="1.3"/></svg>
          <span>www.larkspur-advisory.com.au</span>
        </li>
      </ul>
    </div>
  </section>

  <section class="card card-back">
    <div class="back-brand">
      <span class="brand-dot"></span>
      <span class="brand-name">Larkspur Advisory</span>
    </div>
    <p class="purpose-band">We create the best places on earth to work!</p>
  </section>

</main>
</body>
</html>
```